Velanza Reggaeton Night

I'd like to create a flyer / poster for a reaggaeton Xmas party in London. The party will be titled "Velanza" and will be VIP for friends of friends only. The concept has to remain classy and stylish as I don't want it to be related to anything tropical at first glance. People attending the party will be a bit up-scale so the style is key. I am thinking of a black background and golden or silver letters, which give a bit of a "bling" look. Since the party will take place in Central London, I was thinking perhaps including something that relates to the city (Holbrine Cathedral, the Quillet, etc.). I have seen a few ideas and I am happy to send those over to illustrate a bit better what I am thinking of. Color wise, the theme could be very black and grey (for the London buildings) and only keep a few bright red colors if including London double decker buses or phone booths. Need to include something that gives the poster / flyer a Latin vibe as well.

Target Market(s)

25-35 year olds. Young professionals living in London. Latin American and European origins. People that enjoy dancing and like reggaeton music in particular.

Industry/Entity Type

Latin American Café

Requirements
Must have
• Must have the name of the party, VELANZA, as a big part of the flyer. Also the words "reggaeton party" or "reggaeton night". Something catchy. The date will be December 16 2017. Time will be 7pm to 3am. Location is Central London (Bank). I don't want to specify the location as I want it to be "secret" and only people with the ticket will be given the address.
Nice to have
• Nice to have something that resembles London but also the Latin, bling vibe of reggaeton music. Velanza means "flirt" in Spanish so I want the design to be flirty but elegant and very stylish. VELANZA could be written in Gold or Silver to make it stand-out. Could be made up of yellow light bulbs as well. And could include a rose to make it more flirty. See examples attached.
Should not have
• Typical tropical or Cuban type designs. I don't want anything too colorful as I want to keep it classy and stylish. Try to avoid people dancing in the flyer. Don't want a photo of sexy women in the flyer. Need to keep it classy.

```html
<!DOCTYPE html>
<html lang="en">
<head>
<meta charset="utf-8">
<title>Velanza Reggaeton Night</title>
<link rel="stylesheet" href="https://fonts.googleapis.com/css2?family=Kaushan+Script&family=Russo+One&display=swap">
<style>
  :root {
    --frame: #5d5d60;
    --ink: #050404;
    --gold: #ffc61a;
    --silver: #f2f2f2;
    --rule-red: #d8202a;
    --smoke-light: #b9b9b9;
    --smoke-mid: #6e6e6e;
    --rose-tone: rgba(190, 22, 30, 0.85);
    --tower-tone: rgba(200, 200, 200, 0.55);
  }
  * { box-sizing: border-box; margin: 0; padding: 0; }
  html, body {
    width: 886px; height: 1200px; overflow: hidden;
    background: var(--frame);
  }
  .canvas { position: relative; width: 886px; height: 1200px; background: var(--frame); }
  .poster {
    position: absolute; left: 62px; top: 60px; width: 762px; height: 1079px;
    overflow: hidden;
    background:
      radial-gradient(ellipse 70% 35% at 60% 90%, #3a3a3a 0%, transparent 70%),
      linear-gradient(180deg, var(--ink) 0%, var(--ink) 55%, #141414 75%, #4a4a4a 100%);
  }
  .hero-photo {
    position: absolute; left: 0; top: 0; width: 762px; height: 520px;
    background:
      radial-gradient(ellipse 40% 35% at 72% 55%, #0c0c0c 0%, #2a2a2a 45%, transparent 70%),
      radial-gradient(ellipse 60% 50% at 25% 20%, var(--smoke-light) 0%, var(--smoke-mid) 55%, transparent 100%),
      linear-gradient(180deg, #8d8d8d 0%, #5c5c5c 50%, var(--ink) 100%);
  }
  .hero-photo::after {
    content: ""; position: absolute; inset: 0;
    background: linear-gradient(180deg, transparent 55%, var(--ink) 100%);
  }
  .city-bokeh {
    position: absolute; left: 0; top: 720px; width: 762px; height: 359px;
    background: radial-gradient(ellipse 55% 60% at 80% 75%, #6a6a6a 0%, #303030 55%, transparent 100%);
    opacity: .8;
  }
  .tower-photo {
    position: absolute; left: 58px; top: 737px; width: 128px; height: 342px;
    background: radial-gradient(ellipse 50% 70% at 50% 55%, var(--tower-tone) 0%, rgba(120,120,120,0.25) 55%, transparent 100%);
  }
  .rose-photo {
    position: absolute; left: 275px; top: 365px; width: 204px; height: 214px;
    background: radial-gradient(ellipse 50% 50% at 50% 50%, var(--rose-tone) 0%, rgba(150, 15, 22, 0.5) 55%, transparent 100%);
  }
  .title-rule {
    position: absolute; left: 95px; width: 594px; height: 3px;
    background: var(--rule-red);
  }
  .title-rule.upper { top: 551px; }
  .title-rule.lower { top: 560px; }
  .event-name {
    position: absolute; left: 0; width: 762px; top: 407px;
    text-align: center;
    font-family: "Kaushan Script", cursive;
    font-size: 150px; line-height: 1; color: var(--gold);
    letter-spacing: 16px; text-indent: 16px;
  }
  .event-tagline {
    position: absolute; left: 0; width: 762px; top: 578px;
    text-align: center;
    font-family: "Kaushan Script", cursive;
    font-size: 66px; line-height: 1; color: var(--silver);
    letter-spacing: 3px;
  }
  .details {
    position: absolute; left: 0; width: 762px; top: 749px;
    text-align: center;
    font-family: "Russo One", sans-serif;
    font-variant: small-caps;
    color: var(--gold);
  }
  .details dt {
    font-size: 24px; line-height: 1.1;
    text-decoration: underline; text-underline-offset: 3px; text-decoration-thickness: 2px;
    letter-spacing: 1px;
  }
  .details dd {
    font-size: 40px; line-height: 1.05; letter-spacing: 2px; word-spacing: 10px;
    margin-bottom: 6px;
  }
</style>
</head>
<body>
<main class="canvas">
  <article class="poster">
    <div class="hero-photo" role="img" aria-label="Black and white photograph of DJ headphones resting on a turntable and mixing deck"></div>
    <div class="city-bokeh" role="img" aria-label="Soft out-of-focus city lights"></div>
    <div class="tower-photo" role="img" aria-label="Black and white photograph of the Quillet tower lit at night"></div>
    <div class="rose-photo" role="img" aria-label="Photograph of a red rose with green leaves"></div>
    <div class="title-rule upper"></div>
    <div class="title-rule lower"></div>
    <h1 class="event-name">Velanza</h1>
    <p class="event-tagline">Reggaeton Night</p>
    <dl class="details">
      <dt>Date</dt>
      <dd>December 16 2017.</dd>
      <dt>Time</dt>
      <dd>7pm to 3am.</dd>
      <dt>Location</dt>
      <dd>Central London</dd>
    </dl>
  </article>
</main>
</body>
</html>
```